Wine Label Front & Rear for new release Shiraz

Hi All.
Wine Label Front and Rear Designed please use your own freedom of design with bellow content requirements

Front
Wine Brand Name (Designers Choice, be creative)
Type of Wine= Shiraz
Text that must be included= Wine of Australia (and) 750mls
Label Size= 8.5cm W x 13cm L

Rear
Wine Brand name (Designers choice same as front)
(Room for bar code)
(room for descriptive text)
Size = 7.5cm W x 11.5cm L

Target Market(s)

High End wine lovers

Colors

Designer to choose colors to be used in the design.

Requirements
Must have
• all the content i have mentioned in the product description

```html
<!DOCTYPE html>
<html lang="en">
<head>
<meta charset="utf-8">
<title>Marlowe Ridge Wines — 2013 Shiraz Front Label</title>
<link rel="stylesheet" href="https://fonts.googleapis.com/css2?family=Cinzel:wght@400;600;700&family=Pinyon+Script&display=swap">
<style>
  :root {
    --glass-deep: #0d0506;
    --glass-wine: #1e0b0d;
    --gold: #c9a047;
    --gold-light: #e6c878;
    --gold-dark: #8a6a2a;
  }
  * { margin: 0; padding: 0; box-sizing: border-box; }
  html, body {
    width: 1200px;
    height: 3717px;
    overflow: hidden;
    background: var(--glass-deep);
  }
  .label {
    position: relative;
    width: 1200px;
    height: 3717px;
    background: linear-gradient(90deg, var(--glass-deep) 0%, var(--glass-wine) 50%, var(--glass-deep) 100%);
    display: flex;
    flex-direction: column;
    align-items: center;
    justify-content: center;
    color: var(--gold);
    font-family: "Cinzel", serif;
  }
  .brand-name {
    font-size: 47px;
    font-weight: 600;
    letter-spacing: 2px;
    color: var(--gold);
  }
  .crest {
    width: 812px;
    height: 495px;
    margin-top: 190px;
    border-radius: 40px;
    background: radial-gradient(ellipse at 50% 45%, var(--gold-light) 0%, var(--gold) 40%, var(--gold-dark) 75%, rgba(138,106,42,0) 100%);
    opacity: 0.85;
  }
  .vintage {
    margin-top: 110px;
    font-size: 36px;
    font-weight: 400;
    letter-spacing: 2px;
    color: var(--gold-light);
  }
  .variety {
    margin-top: 10px;
    font-family: "Pinyon Script", cursive;
    font-size: 150px;
    line-height: 1;
    color: var(--gold);
  }
  .wine-name {
    margin-top: 10px;
    font-size: 43px;
    font-weight: 700;
    letter-spacing: 2px;
    color: var(--gold);
  }
  .legal-line {
    width: 730px;
    margin-top: 100px;
    display: flex;
    justify-content: space-between;
    font-size: 22px;
    font-weight: 400;
    letter-spacing: 1px;
    color: var(--gold);
  }
</style>
</head>
<body>
  <main class="label">
    <h1 class="brand-name">MARLOWE RIDGE WINES</h1>
    <div class="crest" role="img" aria-label="Gold heraldic crest with two native animals flanking a shield, star above, grapevines and a ribbon banner"></div>
    <p class="vintage">2013</p>
    <p class="variety">Shiraz</p>
    <p class="wine-name">THE AMBER PATH</p>
    <div class="legal-line">
      <span class="origin">Wine of Australia</span>
      <span class="volume">750ML</span>
    </div>
  </main>
</body>
</html>
```